Long term design collaboration - mobile app design & web app design

We are looking for a talented mobile designer to help us improve our UI & UX for mobile app and web app.

The screens that need to be redesigned are attached.

There is potentially a lot more work in future design available for the successful candidate.
The successful candidate would have to take part in daily stand-up around 3 times per week.
The successful candidate would join a dev team
We are software company that does property management

```html
<!DOCTYPE html>
<html lang="en">
<head>
<meta charset="utf-8">
<title>Hallmere Dashboard</title>
<link href="https://fonts.googleapis.com/css2?family=Poppins:wght@400;500;600;700&display=swap" rel="stylesheet">
<style>
:root{
  --stage:#0c2340;
  --blue:#0b6cc0;
  --cyan:#0aa8ea;
  --ink:#1b2430;
  --muted:#9aa3ad;
  --line:#e8edf2;
  --panel:#f2f5f8;
  --white:#ffffff;
  --green-a:#2fbf71;
  --green-b:#1b86a6;
  --card-b-a:#2a93da;
  --card-b-b:#2e4da6;
  --orange:#f5a623;
  --red:#e53935;
  --pale-blue:#e3f0fb;
  --pale-orange:#fdf0db;
  --pale-green:#dff4e6;
  --pale-red:#fde4e4;
}
*{box-sizing:border-box;margin:0;padding:0}
html,body{width:716px;height:1200px;overflow:hidden;background:var(--stage);font-family:'Poppins',sans-serif;color:var(--ink)}
.canvas{position:relative;width:716px;height:1200px;padding:0 20px}
.section-label{color:var(--cyan);font-size:9px;font-weight:600;letter-spacing:4px;height:18px;display:flex;align-items:center}
.section-label.top{margin-top:18px;margin-bottom:6px}
.section-label.mid{margin-top:24px;margin-bottom:8px}

/* Desktop */
.desk{display:flex;width:676px;height:430px;border-radius:10px;background:linear-gradient(160deg,var(--blue),var(--cyan));overflow:hidden}
.sidebar{width:124px;padding:14px 10px 12px;display:flex;flex-direction:column;color:var(--white)}
.brand{display:flex;align-items:center;gap:6px;font-weight:600;font-size:12px;margin-left:4px}
.brand-mark{width:14px;height:14px;border-radius:3px;background:var(--white)}
.new-report{margin-top:20px;background:var(--white);color:var(--blue);border-radius:14px;height:24px;display:flex;align-items:center;justify-content:center;gap:5px;font-size:7px;font-weight:600}
.new-report i{width:9px;height:9px;border-radius:2px;background:var(--blue)}
.nav{margin-top:14px;display:flex;flex-direction:column;gap:3px}
.nav-item{display:flex;align-items:center;gap:8px;height:21px;padding:0 8px;font-size:6px;border-radius:5px}
.nav-item.active{background:rgba(255,255,255,.18);font-weight:600}
.nav-item i{width:8px;height:8px;border-radius:2px;border:1.3px solid var(--white)}
.nav-badge{margin-left:auto;width:9px;height:9px;border-radius:50%;background:var(--cyan);font-size:5px;display:flex;align-items:center;justify-content:center;border:1px solid rgba(255,255,255,.6)}
.logout{margin-top:auto;font-size:6px;display:flex;gap:8px;padding-left:8px;align-items:center}
.logout i{width:8px;height:7px;border:1.3px solid var(--white);border-left:none}
.copyright{font-size:5px;margin-top:16px;opacity:.8;line-height:1.4;padding-left:2px}
.main{flex:1;margin:8px 8px 8px 0;background:var(--white);border-radius:8px;padding:12px 14px 0;overflow:hidden}
.main-head{display:flex;align-items:center;height:20px}
.main-head h1{font-size:12px;font-weight:600}
.bell{margin-left:auto;position:relative;width:10px;height:10px;border-radius:3px 3px 1px 1px;background:#7d8896}
.bell b{position:absolute;top:-4px;right:-4px;width:7px;height:7px;border-radius:50%;background:var(--cyan)}
.user{display:flex;align-items:center;gap:4px;margin-left:18px}
.avatar{border-radius:50%;background:linear-gradient(135deg,#b48a63,#5b6f86)}
.user .avatar{width:15px;height:15px}
.user-name{font-size:5.5px;font-weight:600;line-height:1.2}
.user-name span{display:block;font-weight:400;color:var(--muted);font-size:4.5px}
.main-body{display:flex;gap:22px;margin-top:8px}
.col-left{width:342px}
.col-right{width:146px;border:1px solid var(--line);border-radius:6px;height:360px;padding:8px}
.cards{display:flex;gap:10px}
.bal-card{width:130px;height:71px;border-radius:5px;padding:10px;color:var(--white);position:relative}
.bal-card.green{background:linear-gradient(135deg,var(--green-a),var(--green-b))}
.bal-card.blue{background:linear-gradient(135deg,var(--card-b-a),var(--card-b-b))}
.bal-head{display:flex;align-items:center;gap:5px;font-size:6px;font-weight:500}
.bal-head i{width:11px;height:11px;border-radius:3px;background:rgba(255,255,255,.25)}
.bal-amt{font-size:10px;font-weight:600;margin-top:9px}
.bal-sub{font-size:4.5px;opacity:.8;margin-top:2px;letter-spacing:.3px}
.dots3{position:absolute;right:8px;top:8px;width:2px;height:7px;border-left:2px dotted var(--white)}
.h2{font-size:9px;font-weight:600;margin:14px 0 7px}
.list{border:1px solid var(--line);border-radius:5px}
.row{display:flex;align-items:center;gap:7px;padding:0 10px;height:30px;border-bottom:1px solid var(--line)}
.row:last-child{border-bottom:none}
.ico{width:13px;height:13px;border-radius:50%;flex:none}
.ico.orange{background:var(--pale-orange);box-shadow:inset 0 0 0 3.5px var(--pale-orange),inset 0 0 0 10px var(--orange)}
.ico.blue{background:var(--pale-blue);box-shadow:inset 0 0 0 3.5px var(--pale-blue),inset 0 0 0 10px var(--blue)}
.ico.green{background:var(--pale-green);box-shadow:inset 0 0 0 3.5px var(--pale-green),inset 0 0 0 10px var(--green-a)}
.ico.red{background:var(--pale-red);box-shadow:inset 0 0 0 3.5px var(--pale-red),inset 0 0 0 10px var(--red)}
.row-text{font-size:6px;font-weight:600;line-height:1.35}
.row-text span{display:block;font-weight:400;color:var(--muted);font-size:5px}
.chev{margin-left:auto;width:4px;height:4px;border-top:1.2px solid var(--blue);border-right:1.2px solid var(--blue);transform:rotate(45deg);flex:none}
.groups{display:flex;gap:12px;margin-top:14px}
.group{flex:1;background:var(--panel);border-radius:6px;padding:8px}
.group-title{display:flex;align-items:center;gap:5px;font-size:7px;font-weight:500;margin-bottom:6px}
.group-title i{width:9px;height:10px;border-radius:2px;background:var(--blue)}
.group-title i.shield{background:var(--green-a);border-radius:2px 2px 5px 5px}
.item{background:var(--white);border-radius:4px;height:26px;display:flex;align-items:center;padding:0 7px;margin-bottom:5px;font-size:5.5px;gap:6px}
.item.ruled{border-left:1.5px solid var(--line)}
.item-text{line-height:1.35}
.item-text span{display:block;color:var(--muted);font-size:4.5px}
.item .ico{width:11px;height:11px}
.tag{margin-left:auto;font-size:4.5px;font-weight:600;border-radius:3px;padding:2px 5px;background:var(--panel);color:#5c6670;white-space:nowrap}
.tag.pending{background:var(--pale-orange);color:var(--orange)}
.tag.overdue{background:var(--pale-red);color:var(--red)}
.item .chev{margin-left:6px}
.setup-title{display:flex;align-items:center;gap:5px;font-size:6px;font-weight:600;padding-bottom:8px;border-bottom:1px solid var(--line)}
.warn{width:0;height:0;border-left:4px solid transparent;border-right:4px solid transparent;border-bottom:7px solid var(--red);flex:none}
.task{display:flex;align-items:center;gap:7px;height:31px;margin-top:2px}
.task .ico{width:10px;height:10px}
.task-text{font-size:5px;font-weight:500;flex:1}
.progress{display:flex;align-items:center;gap:5px;margin-top:3px;font-size:4px;color:var(--muted);font-weight:400}
.bar{width:38px;height:2px;background:var(--line);border-radius:2px;position:relative}
.bar b{position:absolute;left:0;top:0;height:2px;background:var(--cyan);border-radius:2px}

/* Mobile */
.phones{display:flex;gap:36px}
.phone{position:relative;width:320px;height:660px;border-radius:26px;background:#f8fafc;overflow:hidden;border:5px solid #15171c}
.scroll{padding:0 14px}
.status{display:flex;justify-content:space-between;align-items:center;height:34px;padding:0 22px 0 26px;font-size:12px;font-weight:600}
.status-icons{display:flex;gap:4px;align-items:center}
.greet{display:flex;align-items:center;gap:8px;padding:4px 0 10px}
.greet .avatar{width:30px;height:30px}
.greet-text{font-size:10px;color:var(--muted);line-height:1.25}
.greet-text b{display:block;color:var(--ink);font-size:13px;font-weight:600}
.greet-bell{margin-left:auto;width:28px;height:28px;border-radius:50%;background:var(--white);box-shadow:0 1px 4px rgba(0,0,0,.08);position:relative}
.greet-bell b{position:absolute;top:4px;right:4px;width:8px;height:8px;border-radius:50%;background:var(--cyan)}
.m-cards{display:flex;gap:10px;width:420px}
.m-cards .bal-card{width:210px;height:116px;padding:14px;border-radius:6px}
.m-cards .bal-head{font-size:11px;gap:8px}
.m-cards .bal-head i{width:18px;height:18px;border-radius:5px}
.m-cards .bal-amt{font-size:16px;margin-top:20px}
.m-cards .bal-sub{font-size:8px}
.pager{display:flex;justify-content:center;gap:4px;margin:12px 0}
.pager i{width:6px;height:4px;border-radius:2px;background:#c9d6e2}
.pager i.on{width:22px;background:var(--cyan)}
.m-setup{background:var(--panel);border-radius:8px;padding:14px 12px}
.m-setup .setup-title{font-size:11px;border:none;padding:0 0 10px;gap:8px}
.m-setup .warn{border-left-width:7px;border-right-width:7px;border-bottom-width:12px}
.m-task{background:var(--white);border-radius:6px;display:flex;align-items:center;gap:10px;padding:10px 12px}
.m-task .task-text{font-size:9px}
.m-task .progress{font-size:7px;gap:10px}
.m-task .bar{width:70px}
.see-more{margin:12px auto 0;width:84px;height:22px;border:1px solid var(--blue);border-radius:12px;color:var(--blue);font-size:8px;font-weight:600;display:flex;align-items:center;justify-content:center}
.m-h2{font-size:12px;font-weight:600;margin:18px 0 10px}
.m-list{background:var(--white);border-radius:8px;box-shadow:0 1px 3px rgba(0,0,0,.05)}
.m-list .row{height:50px;padding:0 12px;gap:10px}
.m-list .row.tall{height:62px}
.m-list .ico{width:24px;height:24px}
.m-list .row-text{font-size:9.5px}
.m-list .row-text span{font-size:8px}
.m-group{background:var(--panel);border-radius:8px;padding:12px;margin-top:14px}
.m-group .group-title{font-size:11px;margin-bottom:10px;gap:7px}
.m-group .group-title i{width:13px;height:15px}
.m-group .item{height:42px;font-size:9px;padding:0 10px;margin-bottom:7px;border-radius:6px;gap:10px}
.m-group .item-text span{font-size:7px}
.m-group .item .ico{width:20px;height:20px}
.m-group .tag{font-size:7px;padding:3px 8px}
.m-group .chev{margin-left:10px;width:5px;height:5px}
.tabbar{position:absolute;left:0;right:0;bottom:0;height:62px;background:linear-gradient(90deg,var(--blue),var(--cyan));display:flex;justify-content:space-around;padding-top:10px}
.tab{display:flex;flex-direction:column;align-items:center;gap:4px;font-size:7px;color:rgba(255,255,255,.75)}
.tab.on{color:var(--white);font-weight:600}
.tab i{width:13px;height:12px;border:1.5px solid currentColor;border-radius:3px}
.home-bar{position:absolute;left:50%;bottom:7px;transform:translateX(-50%);width:110px;height:3px;border-radius:2px;background:var(--white)}
</style>
</head>
<body>
<div class="canvas">
  <div class="section-label top">DASHBOARD // DESKTOP APP</div>
  <div class="desk">
    <aside class="sidebar">
      <div class="brand"><span class="brand-mark"></span>Hallmere</div>
      <div class="new-report"><i></i>New report</div>
      <nav class="nav">
        <div class="nav-item active"><i></i>Dashboard</div>
        <div class="nav-item"><i></i>User Directory</div>
        <div class="nav-item"><i></i>Messages<span class="nav-badge">8</span></div>
        <div class="nav-item"><i></i>Finances</div>
        <div class="nav-item"><i></i>Switch Development</div>
        <div class="nav-item"><i></i>Sending Letter</div>
        <div class="nav-item"><i></i>Regular Services</div>
      </nav>
      <div class="logout"><i></i>Log out</div>
      <div class="copyright">Copyright © 2024, Hallmere.<br>All Rights Reserved.</div>
    </aside>
    <section class="main">
      <header class="main-head">
        <h1>Dashboard</h1>
        <span class="bell"><b></b></span>
        <div class="user">
          <span class="avatar" role="img" aria-label="User profile photo"></span>
          <div class="user-name">Oliver R.<span>Account role</span></div>
        </div>
      </header>
      <div class="main-body">
        <div class="col-left">
          <div class="cards">
            <div class="bal-card green"><span class="dots3"></span>
              <div class="bal-head"><i></i>Tarnwell Bank</div>
              <div class="bal-amt">$23,261,025.40</div>
              <div class="bal-sub">AVAILABLE BANK BALANCE</div>
            </div>
            <div class="bal-card blue"><span class="dots3"></span>
              <div class="bal-head"><i></i>Property 101</div>
              <div class="bal-amt">$308,285,804.00</div>
              <div class="bal-sub">AVAILABLE PROPERTY BALANCE</div>
            </div>
          </div>
          <div class="h2">General</div>
          <div class="list">
            <div class="row"><span class="ico orange"></span><div class="row-text">28 Jan 2025<span>Handover date</span></div><span class="chev"></span></div>
            <div class="row"><span class="ico blue"></span><div class="row-text">85<span>Units</span></div><span class="chev"></span></div>
            <div class="row"><span class="ico green"></span><div class="row-text">24 Elmstead Road, London, N4 2QT<span>Address</span></div><span class="chev"></span></div>
            <div class="row"><span class="ico red"></span><div class="row-text">£20<span>Section limit</span></div><span class="chev"></span></div>
          </div>
          <div class="groups">
            <div class="group">
              <div class="group-title"><i></i>Compliance</div>
              <div class="item ruled"><div class="item-text">Asbestos<span>-</span></div><span class="tag">⊘ N/A</span><span class="chev"></span></div>
              <div class="item ruled"><div class="item-text">Gutters<span>30 December 2024</span></div><span class="tag pending">◷ PENDING</span><span class="chev"></span></div>
              <div class="item ruled"><div class="item-text">Drains<span>12 December 2024</span></div><span class="tag overdue">▲ OVERDUE</span><span class="chev"></span></div>
              <div class="item ruled"><div class="item-text">Legionellas<span>-</span></div><span class="tag">⊘ N/A</span><span class="chev"></span></div>
            </div>
            <div class="group">
              <div class="group-title"><i class="shield"></i>Insurance</div>
              <div class="item"><span class="ico blue"></span>Terrorism<span class="tag">⊘ N/A</span><span class="chev"></span></div>
              <div class="item"><span class="ico blue"></span>Buildings<span class="tag">⊘ N/A</span><span class="chev"></span></div>
              <div class="item"><span class="ico blue"></span>D &amp; O<span class="tag">⊘ N/A</span><span class="chev"></span></div>
              <div class="item"><span class="ico blue"></span>Engineering<span class="tag">⊘ N/A</span><span class="chev"></span></div>
            </div>
          </div>
        </div>
        <div class="col-right">
          <div class="setup-title"><span class="warn"></span>Please complete basic setup</div>
          <div class="task"><span class="ico blue"></span><div class="task-text">Service Charge Schedules<div class="progress"><span class="bar"><b style="width:30%"></b></span>30% completed</div></div><span class="chev"></span></div>
          <div class="task"><span class="ico blue"></span><div class="task-text">Service Charge Apportionment<div class="progress"><span class="bar"></span>0% completed</div></div><span class="chev"></span></div>
          <div class="task"><span class="ico blue"></span><div class="task-text">Invite Residents and Leaseholders<div class="progress"><span class="bar"><b style="width:60%"></b></span>60% completed</div></div><span class="chev"></span></div>
          <div class="task"><span class="ico blue"></span><div class="task-text">Connect Payment Provider<div class="progress"><span class="bar"></span>0% completed</div></div><span class="chev"></span></div>
        </div>
      </div>
    </section>
  </div>

  <div class="section-label mid">DASHBOARD // MOBILE APP</div>
  <div class="phones">
    <div class="phone">
      <div class="status"><span>9:41</span>
        <span class="status-icons">
          <svg width="16" height="10" viewBox="0 0 16 10"><rect x="0" y="7" width="3" height="3" fill="#1b2430"/><rect x="4" y="5" width="3" height="5" fill="#1b2430"/><rect x="8" y="3" width="3" height="7" fill="#1b2430"/><rect x="12" y="0" width="3" height="10" fill="#1b2430"/></svg>
          <svg width="14" height="10" viewBox="0 0 14 10"><path d="M1 3.5a9 9 0 0 1 12 0M3.5 6a5.5 5.5 0 0 1 7 0" stroke="#1b2430" stroke-width="1.6" fill="none"/><circle cx="7" cy="8.5" r="1.3" fill="#1b2430"/></svg>
          <svg width="22" height="11" viewBox="0 0 22 11"><rect x="0.5" y="0.5" width="19" height="10" rx="3" stroke="#1b2430" fill="none"/><rect x="2" y="2" width="16" height="7" rx="1.5" fill="#1b2430"/><rect x="20.5" y="3.5" width="1.5" height="4" fill="#1b2430"/></svg>
        </span>
      </div>
      <div class="scroll">
        <div class="greet">
          <span class="avatar" role="img" aria-label="User profile photo"></span>
          <div class="greet-text">Good day,<b>Oliver !</b></div>
          <span class="greet-bell"><b></b></span>
        </div>
        <div class="m-cards">
          <div class="bal-card green"><span class="dots3"></span>
            <div class="bal-head"><i></i>Tarnwell Bank</div>
            <div class="bal-amt">$23,261,025.40</div>
            <div class="bal-sub">AVAILABLE BANK BALANCE</div>
          </div>
          <div class="bal-card blue">
            <div class="bal-head"><i></i>Property 101</div>
            <div class="bal-amt">$308,285,804.00</div>
            <div class="bal-sub">AVAILABLE PROPERTY BALANCE</div>
          </div>
        </div>
        <div class="pager"><i class="on"></i><i></i></div>
        <div class="m-setup">
          <div class="setup-title"><span class="warn"></span>Please complete basic setup</div>
          <div class="m-task"><span class="ico blue" style="width:14px;height:14px"></span><div class="task-text">Service Charge Schedules<div class="progress"><span class="bar"><b style="width:30%"></b></span>30% completed</div></div><span class="chev"></span></div>
          <div class="see-more">◉ See more</div>
        </div>
        <div class="m-h2">General</div>
        <div class="m-list">
          <div class="row"><span class="ico orange"></span><div class="row-text">28 Jan 2025<span>Handover date</span></div><span class="chev"></span></div>
          <div class="row"><span class="ico blue"></span><div class="row-text">85<span>Units</span></div><span class="chev"></span></div>
          <div class="row"><span class="ico red"></span><div class="row-text">£20<span>Section limit</span></div><span class="chev"></span></div>
          <div class="row tall"><span class="ico green"></span><div class="row-text">24 Elmstead Road, London,<br>N4 2QT<span>Address</span></div><span class="chev"></span></div>
        </div>
      </div>
      <nav class="tabbar">
        <div class="tab on"><i></i>Dashboard</div>
        <div class="tab"><i></i>User Directory</div>
        <div class="tab"><i></i>Messages</div>
        <div class="tab"><i></i>Finances</div>
        <div class="tab"><i></i>More</div>
      </nav>
      <span class="home-bar"></span>
    </div>

    <div class="phone">
      <div class="scroll" style="padding-top:10px">
        <div class="m-list">
          <div class="row"><span class="ico red"></span><div class="row-text">£20<span>Section limit</span></div><span class="chev"></span></div>
          <div class="row tall"><span class="ico green"></span><div class="row-text">24 Elmstead Road, London,<br>N4 2QT<span>Address</span></div><span class="chev"></span></div>
        </div>
        <div class="m-group">
          <div class="group-title"><i></i>Compliance</div>
          <div class="item ruled"><div class="item-text">Asbestos<span>-</span></div><span class="tag">⊘ N/A</span><span class="chev"></span></div>
          <div class="item ruled"><div class="item-text">Gutters<span>30 December 2024</span></div><span class="tag pending">◷ PENDING</span><span class="chev"></span></div>
          <div class="item ruled"><div class="item-text">Drains<span>12 December 2024</span></div><span class="tag overdue">▲ OVERDUE</span><span class="chev"></span></div>
          <div class="item ruled"><div class="item-text">Legionellas<span>-</span></div><span class="tag">⊘ N/A</span><span class="chev"></span></div>
          <div class="item ruled"><div class="item-text">Dry Risers<span>-</span></div><span class="tag">⊘ N/A</span><span class="chev"></span></div>
        </div>
        <div class="m-group">
          <div class="group-title"><i class="shield"></i>Insurance</div>
          <div class="item"><span class="ico blue"></span>Terrorism<span class="tag">⊘ N/A</span><span class="chev"></span></div>
          <div class="item"><span class="ico blue"></span>Buildings<span class="tag">⊘ N/A</span><span class="chev"></span></div>
          <div class="item"><span class="ico blue"></span>D &amp; O<span class="tag">⊘ N/A</span><span class="chev"></span></div>
          <div class="item"><span class="ico blue"></span>Engineering<span class="tag">⊘ N/A</span><span class="chev"></span></div>
          <div class="item"><span class="ico blue"></span>Reinstatement<span class="tag">⊘ N/A</span><span class="chev"></span></div>
        </div>
      </div>
      <nav class="tabbar">
        <div class="tab on"><i></i>Dashboard</div>
        <div class="tab"><i></i>User Directory</div>
        <div class="tab"><i></i>Messages</div>
        <div class="tab"><i></i>Finances</div>
        <div class="tab"><i></i>More</div>
      </nav>
      <span class="home-bar"></span>
    </div>
  </div>
</div>
</body>
</html>
```